Visitenkarten-Design für Immobilien-Unternehmen
Zielgruppe
Die TORVEL Immobilien GmbH ist eine durch Ing. Gregor Lindqvist inhabergeführte Gesellschaft, welche sich schwerpunktmäßig mit Immobilieninvestitionen sowie Beteiligungen im Bereich von Wohn- und Gewerbeimmobilien beschäftigt. Das Unternehmen kauft, hält, vermietet und verkauft Liegenschaften aller Art, mit dem Fokus auf Gewerbe- und Wohnimmobilien. Zielgruppe sind Personen, welche Immobilien verkaufen möchten - wir betreiben nur eigene Vermögensverwaltung
siehe: www.torvel-immobilien.example
Aufgabenstellung
schlicht und einfach gehalten - weniger ist mehr - nur die wichtigsten Informationen auf der Visitenkarte.
siehe Homepage: www.torvel-immobilien.example

```html
<!DOCTYPE html>
<html lang="de">
<head>
<meta charset="utf-8">
<title>TORVEL Immobilien GmbH – Visitenkarten</title>
<link rel="stylesheet" href="https://fonts.googleapis.com/css2?family=Ubuntu:wght@300;400;500;700&display=swap">
<style>
  :root {
    --ink: #333132;
    --paper: #ffffff;
    --bg: #ffffff;
    --muted: #d9d9d9;
    --shadow: rgba(0,0,0,0.45);
  }
  * { box-sizing: border-box; margin: 0; padding: 0; }
  html, body { width: 1200px; height: 1174px; overflow: hidden; background: var(--bg); }
  body { position: relative; font-family: "Ubuntu", sans-serif; color: var(--ink); }

  .card {
    position: absolute;
    width: 517px;
    overflow: hidden;
    box-shadow: 10px 12px 14px var(--shadow);
  }
  .card--front { height: 292px; background: var(--ink); color: var(--paper); }
  .card--back  { height: 296px; background: var(--paper); }

  .brand { position: absolute; font-family: "Ubuntu", sans-serif; font-weight: 400; text-align: center; }
  .brand__name { display: block; letter-spacing: 2px; line-height: 1; }
  .brand__sub  { display: block; letter-spacing: 2px; line-height: 1; }

  .card--front .brand { left: 0; right: 0; top: 110px; }
  .card--front .brand__name { font-size: 60px; }
  .card--front .brand__sub  { font-size: 16px; margin-top: 14px; color: var(--muted); }

  .card--back .brand { right: 34px; top: 46px; text-align: right; color: var(--ink); }
  .card--back .brand__name { font-size: 38px; letter-spacing: 1px; }
  .card--back .brand__sub  { font-size: 11px; margin-top: 8px; letter-spacing: 1px; }

  .web {
    position: absolute; left: 0; right: 0;
    text-align: center; font-size: 11.5px; font-weight: 700; letter-spacing: 2.2px;
  }
  .card--front .web { top: 249px; color: var(--paper); }
  .web-band {
    position: absolute; left: 0; right: 0; bottom: 0; height: 35px;
    background: var(--paper);
  }
  .web-band .web { top: 10px; color: var(--ink); }

  .person { position: absolute; left: 34px; }
  .person__name { font-size: 20px; font-weight: 500; }
  .person__role { font-size: 8.5px; font-weight: 700; letter-spacing: 1px; margin-top: 6px; }

  .contacts { position: absolute; left: 34px; list-style: none; font-size: 11.5px; font-weight: 500; }
  .contacts li { display: flex; align-items: center; height: 18px; }
  .contacts svg { width: 10px; height: 10px; margin-right: 10px; fill: var(--ink); }

  .address { position: absolute; right: 31px; text-align: right; font-size: 11.5px; font-weight: 500; line-height: 15px; font-style: normal; }

  .footer-band { position: absolute; left: 0; bottom: 0; width: 517px; height: 28px; }
</style>
</head>
<body>

  <!-- Vorderseite mit Webband -->
  <section class="card card--front" style="left:619px; top:120px;">
    <div class="brand"><span class="brand__name">TORVEL</span><span class="brand__sub">IMMOBILIEN GMBH</span></div>
    <div class="web-band"><p class="web">www.torvel-immobilien.example</p></div>
  </section>

  <!-- Vorderseite ohne Web -->
  <section class="card card--front" style="left:57px; top:485px;">
    <div class="brand"><span class="brand__name">TORVEL</span><span class="brand__sub">IMMOBILIEN GMBH</span></div>
  </section>

  <!-- Vorderseite mit Web -->
  <section class="card card--front" style="left:619px; top:485px;">
    <div class="brand"><span class="brand__name">TORVEL</span><span class="brand__sub">IMMOBILIEN GMBH</span></div>
    <p class="web">www.torvel-immobilien.example</p>
  </section>

  <!-- Rückseite mit Web -->
  <section class="card card--back" style="left:57px; top:808px;">
    <div class="brand"><span class="brand__name">TORVEL</span><span class="brand__sub">IMMOBILIEN GMBH</span></div>
    <div class="person" style="top:132px;">
      <p class="person__name">Lindqvist Gregor</p>
      <p class="person__role">GESCHÄFTSFÜHRER</p>
    </div>
    <ul class="contacts" style="top:200px;">
      <li><svg viewBox="0 0 10 10"><path d="M3 0h4a1 1 0 0 1 1 1v8a1 1 0 0 1-1 1H3a1 1 0 0 1-1-1V1a1 1 0 0 1 1-1zm0 1.5v6h4v-6z"/></svg>+43 664 480 27 15</li>
      <li><svg viewBox="0 0 10 10"><path d="M0 2h10v1L5 6 0 3zM0 4l5 3 5-3v4H0z"/></svg>buero@torvel-immobilien.example</li>
      <li><svg viewBox="0 0 10 10"><circle cx="5" cy="5" r="4.5"/><path d="M0.5 5h9M5 0.5v9" stroke="#fff" stroke-width="0.8"/><ellipse cx="5" cy="5" rx="2" ry="4.5" fill="none" stroke="#fff" stroke-width="0.8"/></svg>www.torvel-immobilien.example</li>
    </ul>
    <address class="address" style="top:199px;">Lindenweg 14/3<br>8010 Musterdorf</address>
    <svg class="footer-band" viewBox="0 0 517 28" aria-hidden="true"><polygon points="0,16 340,16 364,2 517,2 517,28 0,28" fill="var(--ink)"/></svg>
  </section>

  <!-- Rückseite ohne Web -->
  <section class="card card--back" style="left:619px; top:808px;">
    <div class="brand"><span class="brand__name">TORVEL</span><span class="brand__sub">IMMOBILIEN GMBH</span></div>
    <div class="person" style="top:137px;">
      <p class="person__name">Lindqvist Gregor</p>
      <p class="person__role">GESCHÄFTSFÜHRER</p>
    </div>
    <ul class="contacts" style="top:212px;">
      <li><svg viewBox="0 0 10 10"><path d="M3 0h4a1 1 0 0 1 1 1v8a1 1 0 0 1-1 1H3a1 1 0 0 1-1-1V1a1 1 0 0 1 1-1zm0 1.5v6h4v-6z"/></svg>+43 664 480 27 15</li>
      <li><svg viewBox="0 0 10 10"><path d="M0 2h10v1L5 6 0 3zM0 4l5 3 5-3v4H0z"/></svg>buero@torvel-immobilien.example</li>
    </ul>
    <address class="address" style="top:209px;">Lindenweg 14/3<br>8010 Musterdorf</address>
    <svg class="footer-band" viewBox="0 0 517 28" aria-hidden="true"><polygon points="0,16 340,16 364,2 517,2 517,28 0,28" fill="var(--ink)"/></svg>
  </section>

</body>
</html>
```